Business Card Design Project

Design a business card for a new entity that is in the OTC (over-the-counter-derivative brokering business-Financial Services.
The card should be clean a professional looking. We encourage designers to think pro-actively, fresh and innovative, but also keep in mind that only 2 things are important. a)that the card look professional b)that it is somehow memorable.

We have a new logo which we will upload and will want the Trident symbol in the logo to be raised OR not have the symbol raised and plan on having the word " BROKERAGE SERVICES" raised that stands out and will look sharp.

Along with uploading the new logo which MUST be incorperated, I am also going to upload 3 different business cards of other businesses to use only as guild-lines since I think they are clean and professional looking BUT I encourage all to be pro-active and creative on their own.

Industry/Entity Type

Business

Requirements
Must have
• 1. MUST HAVE THE NEW LOGO WHICH WILL BE UPLOADED
2. MUST HAVE A VERSION SIMILAR TO THE 3 DIFFERENT BUSINESS CARDS I WILL UPLOAD, BUT EACH DESIGNER MUST ONLY THESE THIS FORMAT AS A BACK-UP AND BE CREATIVE ON THEIR OWN FIRST. ALSO WHEN LOOKING AT THE CARDS WHICH I UPLOAD TO USE AS A GUILD-LINE KEEP IN MIND THAT THESE ARE KESTRAVEL 300 COMPANIES SO DO NOT MIMIC ONLY USE FOR IDEAS.
Nice to have
• these are the 3 different other biz cards to look at for some reference

```html
<!DOCTYPE html>
<html lang="en">
<head>
<meta charset="utf-8">
<title>Halvern Brokerage Services – Business Card</title>
<link rel="stylesheet" href="https://fonts.googleapis.com/css2?family=Open+Sans:wght@400;600&display=swap">
<style>
  :root {
    --backdrop: #1c1c1c;
    --card: #f4f5f6;
    --card-shade: #e3e5e7;
    --gold: #e9b421;
    --gold-deep: #c8941a;
    --ink: #3a3b3d;
    --ink-soft: #6d6e70;
  }
  * { box-sizing: border-box; margin: 0; padding: 0; }
  html, body { width: 1200px; height: 900px; overflow: hidden; }
  body {
    background: var(--backdrop);
    font-family: "Open Sans", Arial, sans-serif;
    color: var(--ink);
    position: relative;
  }
  .card {
    position: absolute;
    left: 250px;
    width: 700px;
    height: 400px;
    background: radial-gradient(ellipse at 40% 40%, #ffffff 0%, var(--card) 55%, var(--card-shade) 100%);
    overflow: hidden;
  }
  .card--front { top: 40px; }
  .card--back { top: 460px; }
  .card__accents { position: absolute; inset: 0; width: 100%; height: 100%; }

  .brand { display: flex; align-items: center; gap: 12px; }
  .brand__square { width: 20px; height: 20px; background: var(--gold); flex: none; }
  .brand__name {
    font-weight: 600;
    color: var(--ink);
    letter-spacing: 2px;
    line-height: 1.25;
    text-transform: uppercase;
    white-space: nowrap;
  }

  .card--front .brand { position: absolute; left: 60px; top: 225px; }
  .card--front .brand__name { font-size: 22px; }

  .holder { position: absolute; left: 450px; top: 70px; }
  .holder__name { font-size: 24px; font-weight: 400; color: var(--ink); }
  .holder__title { font-size: 14px; color: var(--ink-soft); margin-top: 2px; }

  .contacts { list-style: none; position: absolute; left: 450px; top: 150px; }
  .contacts__item {
    display: flex; align-items: center; gap: 8px;
    font-size: 15px; color: var(--ink); margin-bottom: 10px;
    white-space: nowrap;
  }
  .contacts__icon { width: 18px; height: 18px; flex: none; }

  .card--back .brand { position: absolute; left: 50%; top: 150px; transform: translateX(-50%); }
  .card--back .brand__name { font-size: 28px; }
  .website {
    position: absolute; left: 0; right: 0; top: 225px;
    text-align: center; font-size: 17px; color: var(--ink);
  }
</style>
</head>
<body>

<section class="card card--front" aria-label="Card front">
  <svg class="card__accents" viewBox="0 0 700 400" aria-hidden="true">
    <polygon points="0,0 180,0 150,22 0,22" fill="var(--gold)"/>
    <polygon points="0,0 22,0 22,130 0,160" fill="var(--gold-deep)"/>
    <polygon points="0,400 0,250 22,275 22,400" fill="var(--gold)"/>
    <polygon points="0,378 150,378 175,400 0,400" fill="var(--gold-deep)"/>
    <polygon points="560,0 700,0 700,18 585,18" fill="var(--gold)"/>
  </svg>

  <div class="brand">
    <span class="brand__square"></span>
    <span class="brand__name">Halvern<br>Brokerage Services</span>
  </div>

  <div class="holder">
    <p class="holder__name">Your Name</p>
    <p class="holder__title">job title</p>
  </div>

  <ul class="contacts">
    <li class="contacts__item">
      <svg class="contacts__icon" viewBox="0 0 18 18" aria-hidden="true"><rect width="18" height="18" rx="2" fill="var(--gold)"/><rect x="4" y="5" width="10" height="8" fill="none" stroke="#fff" stroke-width="1.4"/><polyline points="4,5 9,10 14,5" fill="none" stroke="#fff" stroke-width="1.4"/></svg>
      name@domainname.com
    </li>
    <li class="contacts__item">
      <svg class="contacts__icon" viewBox="0 0 18 18" aria-hidden="true"><rect width="18" height="18" rx="2" fill="var(--gold)"/><path d="M5 4h3l1 3-2 1a7 7 0 0 0 3 3l1-2 3 1v3c-5 1-10-4-9-9z" fill="#fff"/></svg>
      000-000-0000
    </li>
    <li class="contacts__item">
      <svg class="contacts__icon" viewBox="0 0 18 18" aria-hidden="true"><rect width="18" height="18" rx="2" fill="var(--gold)"/><rect x="4" y="7" width="10" height="7" fill="#fff"/><rect x="6" y="4" width="6" height="3" fill="#fff"/></svg>
      0000-000-0000
    </li>
    <li class="contacts__item">
      <svg class="contacts__icon" viewBox="0 0 18 18" aria-hidden="true"><rect width="18" height="18" rx="2" fill="var(--gold)"/><path d="M9 3a4 4 0 0 1 4 4c0 3-4 8-4 8S5 10 5 7a4 4 0 0 1 4-4z" fill="#fff"/><circle cx="9" cy="7" r="1.5" fill="var(--gold)"/></svg>
      State, Country, Zip Code
    </li>
  </ul>
</section>

<section class="card card--back" aria-label="Card back">
  <svg class="card__accents" viewBox="0 0 700 400" aria-hidden="true">
    <polygon points="700,170 700,400 672,400 672,200" fill="var(--gold)"/>
    <polygon points="700,372 520,372 545,400 700,400" fill="var(--gold-deep)"/>
  </svg>

  <div class="brand">
    <span class="brand__square"></span>
    <span class="brand__name">Halvern Brokerage Services</span>
  </div>
  <p class="website">www.websitename.com</p>
</section>

</body>
</html>
```